We need a completed book cover (front and back) for a Christian devotional book titled "Walking Steady Onward: Shaped as an Open PATH Follower" by Dr. Martin Hale. The publishing company should be "Open Path" (https://opnpathhub.org). This will be for small groups to go through together daily to understand how to grow as a Christian as a part of the family of God. I'm attaching the Open Path logo and the introduction to the book.
Main themes include navigating today’s culture, understanding and using our spiritual gifts, and experiencing joy in community.

```html
<!DOCTYPE html>
<html lang="en">
<head>
<meta charset="utf-8">
<title>Walking Steady Onward — Book Cover</title>
<link rel="stylesheet" href="https://fonts.googleapis.com/css2?family=Libre+Baskerville:wght@400;700&family=Figtree:wght@400;500;600;700&display=swap">
<style>
  :root {
    --paper: #eee3cf;
    --paper-edge: #e3d6be;
    --navy: #2d4c79;
    --teal: #3eaebd;
    --ink: #2b2b2b;
    --rule: #a09c96;
    --avatar-bg: #f2c877;
    --art-light: #8fbf74;
    --art-mid: #5f9a4a;
    --art-base: #b8c4a0;
    --white: #ffffff;
  }
  * { box-sizing: border-box; margin: 0; padding: 0; }
  html, body { width: 1200px; height: 843px; overflow: hidden; }
  body { background: var(--paper); font-family: "Figtree", sans-serif; color: var(--ink); }

  .cover {
    position: relative; width: 1200px; height: 843px; overflow: hidden;
    background: radial-gradient(ellipse at center, var(--paper) 60%, var(--paper-edge) 100%);
  }

  /* Back cover */
  .rule { position: absolute; left: 52px; width: 466px; height: 1px; background: var(--rule); }
  .rule--top { top: 83px; }
  .rule--mid { top: 523px; }
  .rule--low { top: 670px; }

  .back-title {
    position: absolute; left: 64px; top: 98px;
    font-weight: 500; font-size: 26.5px; line-height: 31px; color: var(--teal);
  }
  .back-blurb {
    position: absolute; left: 65px; top: 184px; width: 452px;
    font-size: 13px; line-height: 26.6px; color: var(--ink);
  }

  .author-avatar { position: absolute; left: 63px; top: 537px; width: 122px; height: 122px; }
  .author-heading {
    position: absolute; left: 212px; top: 534px;
    font-weight: 700; font-size: 14px; color: var(--teal);
  }
  .author-bio {
    position: absolute; left: 212px; top: 555px; width: 258px;
    font-size: 11px; line-height: 21.5px;
  }

  .imprint { position: absolute; display: flex; flex-direction: column; align-items: center; gap: 8px; }
  .imprint__dot { width: 12px; height: 12px; border-radius: 50%; background: var(--teal); }
  .imprint__name { font-weight: 600; font-size: 15px; color: #7d7a76; white-space: nowrap; letter-spacing: 0.5px; }
  .imprint--back { left: 60px; top: 708px; }
  .imprint--spine { left: 562px; top: 708px; }

  .acquire-info {
    position: absolute; left: 163px; top: 689px;
    font-size: 11.5px; line-height: 17.8px; color: #4a4a4a;
  }
  .isbn-box {
    position: absolute; left: 338px; top: 688px; width: 180px; height: 111px;
    background: var(--white); text-align: center;
    font-size: 12.5px; line-height: 25px; padding-top: 6px; color: #333;
  }

  /* Spine */
  .spine-title, .spine-subtitle, .spine-author {
    position: absolute; writing-mode: vertical-rl; white-space: nowrap;
  }
  .spine-title {
    left: 601px; top: 95px;
    font-family: "Libre Baskerville", serif; font-size: 22px; color: var(--navy);
    letter-spacing: 1px; line-height: 26px;
  }
  .spine-subtitle {
    left: 571px; top: 121px;
    font-weight: 600; font-size: 15px; color: var(--teal); letter-spacing: 2px; line-height: 20px;
  }
  .spine-author {
    left: 583px; top: 568px;
    font-family: "Libre Baskerville", serif; font-size: 30px; color: var(--navy); line-height: 34px;
  }

  /* Front cover */
  .front-title {
    position: absolute; left: 655px; width: 520px; top: 60px; text-align: center;
    font-family: "Libre Baskerville", serif; font-weight: 400;
    font-size: 64px; line-height: 81px; color: var(--navy); letter-spacing: 2px;
  }
  .front-subtitle {
    position: absolute; left: 655px; width: 520px; top: 318px; text-align: center;
    font-weight: 700; font-size: 21px; color: var(--teal); letter-spacing: 2.6px; white-space: nowrap;
  }
  .cover-art {
    position: absolute; left: 672px; top: 368px; width: 450px; height: 326px;
    border-radius: 6px;
    background: linear-gradient(180deg, var(--art-light) 0%, var(--art-mid) 70%, var(--art-base) 100%);
  }
  .front-author {
    position: absolute; left: 655px; width: 520px; top: 698px; text-align: center;
    font-family: "Libre Baskerville", serif; font-weight: 700;
    font-size: 52px; line-height: 60px; color: var(--navy); letter-spacing: -1px; white-space: nowrap;
  }
  .front-role {
    position: absolute; left: 655px; width: 520px; top: 760px; text-align: center;
    font-weight: 700; font-size: 20px; color: var(--teal); letter-spacing: 7.5px;
  }
</style>
</head>
<body>
<main class="cover">

  <!-- Back cover -->
  <div class="rule rule--top"></div>
  <h2 class="back-title">Walking Steady Onward:<br>Shaped as an "Open PATH" Follower</h2>
  <p class="back-blurb">Inviting Jesus to live in your daily life is the most fulfilling opportunity you may ever take on. If you are someone re-committing your life to Him after a season away, and you are serious this time, you may be surprised with what He has in store for you in these pages. &nbsp;Either way, discovering God’s purposes for your day-to-day life will find great fulfillment in the pages of Walking Steady Onward. &nbsp;You have the chance to discover a new level of personal growth as you know Him more and more. &nbsp;You also will understand that He has prepared a life-giving community around you, the place He brings change in every one of our lives. &nbsp;Yes, walking the Open PATH as you grow in Christ will take you on a most unusual adventure. &nbsp;In fact, we hope that you actually go through this devotional with two or three others to bring the Open PATH realities home immediately in your life.</p>
  <div class="rule rule--mid"></div>

  <svg class="author-avatar" viewBox="0 0 122 122" role="img" aria-label="Author photo placeholder">
    <circle cx="61" cy="61" r="58" fill="var(--avatar-bg)" stroke="var(--teal)" stroke-width="5"/>
    <circle cx="61" cy="37" r="24" fill="var(--teal)"/>
    <path d="M32 110 V86 a29 29 0 0 1 58 0 V110 Z" fill="var(--teal)"/>
  </svg>
  <h3 class="author-heading">About the author</h3>
  <p class="author-bio">Lorem ipsum dolor sit amet, consectetur adipiscing elit, sed do eiusmod tempor incididunt ut labore et dolore magna aliqua. Quis ipsum suspendisse ultrices gravida. Risus commodo viverra maecenas accumsan lacus vel facilisis.</p>
  <div class="rule rule--low"></div>

  <div class="imprint imprint--back">
    <span class="imprint__dot"></span>
    <span class="imprint__name">Open PATH</span>
  </div>
  <p class="acquire-info">address and/or<br>information on how<br>to acquire this<br>novel goes here</p>
  <div class="isbn-box">ISBN Number<br>&amp; barcode go here</div>

  <!-- Spine -->
  <span class="spine-title">WALKING STEADY ONWARD:</span>
  <span class="spine-subtitle">SHAPED AS AN "OPEN PATH" FOLLOWER</span>
  <span class="spine-author">Hale</span>
  <div class="imprint imprint--spine">
    <span class="imprint__dot"></span>
    <span class="imprint__name">Open PATH</span>
  </div>

  <!-- Front cover -->
  <h1 class="front-title">WALKING<br>STEADY<br>ONWARD:</h1>
  <p class="front-subtitle">SHAPED AS AN "OPEN PATH" FOLLOWER</p>
  <div class="cover-art" role="img" aria-label="Cover illustration area: a broad leafy green tree standing on a patch of grass"></div>
  <p class="front-author">Dr. Martin Hale</p>
  <p class="front-role">GENERAL EDITOR</p>

</main>
</body>
</html>
```